A premier branding design firm seeks pro designer for a cargo van wrap design

A school for adults pursuing careers in the medical field as medical assistants is seeking a cargo van wrap design that reflects its professionalism and commitment to high-quality training. The design should embody a corporate, high-end aesthetic with clean lines, modern visuals, and a polished layout that communicates trust, credibility, and advancement. By combining a sleek color palette, (See fonts and provided color call outs on the attached Brand Sheet) contemporary typography, the wrap should present the school as a premier institution for adult learners preparing for meaningful roles in healthcare.
(2009 Marlo Cargo Van 2500 full wrap)

```html
<!DOCTYPE html>
<html lang="en">
<head>
<meta charset="utf-8">
<title>Harborview Adult School – Cargo Van Wrap</title>
<link href="https://fonts.googleapis.com/css2?family=Montserrat:wght@500&family=Nunito:wght@600;700&display=swap" rel="stylesheet">
<style>
  :root{
    --orange:#e0873a;
    --sky:#80a9bb;
    --teal:#3f9a8f;
    --ink:#7b7e82;
    --paper:#ffffff;
    --stage:#f2f2f2;
    --edge:#d9dadc;
    --photo-light:#eceeef;
    --photo-dark:#b9bcbf;
  }
  *{margin:0;padding:0;box-sizing:border-box}
  html,body{width:931px;height:1200px;overflow:hidden;background:var(--stage)}
  .canvas{position:relative;width:931px;height:1200px}
  .panel{position:absolute;display:block}
  .side-driver{left:48px;top:40px}
  .side-passenger{left:48px;top:345px}
  .rear{left:86px;top:690px}
  .hood{left:500px;top:740px}
  .wordmark{font-family:"Montserrat",sans-serif;font-weight:500;fill:var(--ink);letter-spacing:.16em}
  .tagline{font-family:"Nunito",sans-serif;font-weight:600;fill:var(--paper)}
  .contact{font-family:"Nunito",sans-serif;font-weight:700;fill:var(--paper)}
  .panel-edge{fill:var(--paper);stroke:var(--edge);stroke-width:1}
</style>
</head>
<body>
<main class="canvas">

  <!-- Driver side -->
  <svg class="panel side-driver" width="836" height="253" viewBox="0 0 760 230">
    <defs>
      <clipPath id="driver-clip"><rect width="760" height="230" rx="14"/></clipPath>
      <linearGradient id="photo-tone" x1="0" y1="0" x2="0" y2="1">
        <stop offset="0" stop-color="var(--photo-light)"/>
        <stop offset="1" stop-color="var(--photo-dark)"/>
      </linearGradient>
    </defs>
    <rect class="panel-edge" x=".5" y=".5" width="759" height="229" rx="14"/>
    <g clip-path="url(#driver-clip)">
      <path fill="var(--orange)" d="M200 230 L300 116 Q312 103 330 103 L575 103 L575 230 Z"/>
      <path fill="var(--sky)" d="M216 230 L314 130 Q324 120 342 120 L575 120 L575 230 Z"/>
      <path fill="var(--paper)" d="M230 230 L326 144 Q334 138 350 138 L575 138 L575 230 Z"/>
      <path fill="var(--teal)" d="M236 230 L330 150 Q338 143 354 143 L575 143 L575 230 Z"/>
      <rect x="575" y="0" width="185" height="230" fill="url(#photo-tone)" role="img" aria-label="Photo of a smiling medical instructor in a white lab coat"/>
    </g>
    <text class="tagline" x="426" y="116" font-size="13" text-anchor="middle">Your Career</text>
    <text class="tagline" x="452" y="135" font-size="12.5" text-anchor="middle">Starts Here!</text>
    <text class="contact" x="418" y="183" font-size="16" text-anchor="middle">+1 555-014-4227</text>
    <text class="contact" x="418" y="204" font-size="17" text-anchor="middle">www.hvas.edu</text>
    <rect x="336" y="18" width="64" height="64" rx="4" fill="var(--orange)"/>
    <text class="wordmark" font-size="14"><tspan x="418" y="31">HARBORVIEW</tspan><tspan x="418" y="49">ADULT</tspan><tspan x="418" y="67">SCHOOL</tspan></text>
    <rect x="175" y="124" width="32" height="32" rx="2" fill="var(--orange)"/>
    <text class="wordmark" font-size="7.5"><tspan x="215" y="132">HARBORVIEW</tspan><tspan x="215" y="142">ADULT</tspan><tspan x="215" y="152">SCHOOL</tspan></text>
  </svg>

  <!-- Passenger side -->
  <svg class="panel side-passenger" width="836" height="253" viewBox="0 0 760 230">
    <defs>
      <clipPath id="passenger-clip"><rect width="760" height="230" rx="14"/></clipPath>
    </defs>
    <rect class="panel-edge" x=".5" y=".5" width="759" height="229" rx="14"/>
    <g clip-path="url(#passenger-clip)">
      <g transform="translate(760 0) scale(-1 1)">
        <path fill="var(--orange)" d="M200 230 L300 116 Q312 103 330 103 L575 103 L575 230 Z"/>
        <path fill="var(--sky)" d="M216 230 L314 130 Q324 120 342 120 L575 120 L575 230 Z"/>
        <path fill="var(--paper)" d="M230 230 L326 144 Q334 138 350 138 L575 138 L575 230 Z"/>
        <path fill="var(--teal)" d="M236 230 L330 150 Q338 143 354 143 L575 143 L575 230 Z"/>
      </g>
      <rect x="0" y="0" width="185" height="230" fill="url(#photo-tone)" role="img" aria-label="Photo of a smiling medical instructor in a white lab coat"/>
    </g>
    <text class="tagline" x="282" y="116" font-size="13" text-anchor="middle">Your Career</text>
    <text class="tagline" x="304" y="135" font-size="12.5" text-anchor="middle">Starts Here!</text>
    <text class="contact" x="330" y="183" font-size="16" text-anchor="middle">+1 555-014-4227</text>
    <text class="contact" x="330" y="204" font-size="17" text-anchor="middle">www.hvas.edu</text>
    <rect x="204" y="18" width="64" height="64" rx="4" fill="var(--orange)"/>
    <text class="wordmark" font-size="14"><tspan x="286" y="31">HARBORVIEW</tspan><tspan x="286" y="49">ADULT</tspan><tspan x="286" y="67">SCHOOL</tspan></text>
    <rect x="483" y="124" width="32" height="32" rx="2" fill="var(--orange)"/>
    <text class="wordmark" font-size="7.5"><tspan x="523" y="132">HARBORVIEW</tspan><tspan x="523" y="142">ADULT</tspan><tspan x="523" y="152">SCHOOL</tspan></text>
  </svg>

  <!-- Rear doors -->
  <svg class="panel rear" width="330" height="242" viewBox="0 0 280 205">
    <defs>
      <clipPath id="rear-clip"><rect width="280" height="205" rx="12"/></clipPath>
    </defs>
    <rect class="panel-edge" x=".5" y=".5" width="279" height="204" rx="12"/>
    <g clip-path="url(#rear-clip)">
      <rect x="0" y="101" width="280" height="18" fill="var(--orange)"/>
      <rect x="0" y="121" width="280" height="18" fill="var(--sky)"/>
      <rect x="0" y="143" width="280" height="62" fill="var(--teal)"/>
    </g>
    <text class="tagline" x="120" y="115" font-size="12" text-anchor="middle">Your Career</text>
    <text class="tagline" x="100" y="135" font-size="11.5" text-anchor="middle">Starts Here!</text>
    <text class="contact" x="25" y="170" font-size="11">+1 555-014-4227</text>
    <text class="contact" x="25" y="184" font-size="12">www.hvas.edu</text>
    <rect x="56" y="30" width="52" height="52" rx="3" fill="var(--orange)"/>
    <text class="wordmark" font-size="10.5"><tspan x="122" y="44">HARBORVIEW</tspan><tspan x="122" y="60">ADULT</tspan><tspan x="122" y="76">SCHOOL</tspan></text>
  </svg>

  <!-- Hood -->
  <svg class="panel hood" width="360" height="132" viewBox="0 0 300 110">
    <rect class="panel-edge" x=".5" y=".5" width="299" height="109" rx="16"/>
    <rect x="78" y="36" width="36" height="36" rx="2" fill="var(--orange)"/>
    <text class="wordmark" font-size="8.5"><tspan x="124" y="46">HARBORVIEW</tspan><tspan x="124" y="58">ADULT</tspan><tspan x="124" y="70">SCHOOL</tspan></text>
  </svg>

</main>
</body>
</html>
```